A colourful crystal mystical tapestry

I need an image for my book cover. The title of the book is The Woven Lantern . Below, the subtitle is Along Quiet Rivers. The crystals move from bottom right to one third up the cover and into the middle. Stop below book title. (Book is 9x6). The crystals have to look like a multi-colour tapestry. Real crystals appear like they are gently exploding from the bottom right of the cover. More like movement than rocketships pls. But not a bunch of fragments. More clustered together. The upper cover will be white. They crystals are multi-covered bright - shinning. It can not be a bad AI image. It must be sharp and brilliant - a tapestry of colours. It is a spiritual book so, it needs to feel as such. If another creative idea comes to mind...give it a try.. I am open to something completely different as long as if is a multi-colour adult appealing spiritual unique image- which represents the title well. THANKS in advance.

Target Market(s)

Readers of multi-dimensional stories. ADULTS

Industry/Entity Type

Spirituality. Beautiful interesting intriguing.

Requirements
Nice to have
• It's tapestry, not chaos per say.
Should not have
• Anything crappy space like AI I can easily create. Be unique.

```html
<!DOCTYPE html>
<html lang="en">
<head>
<meta charset="UTF-8">
<title>The Woven Lantern — Cover Options</title>
<link rel="stylesheet" href="https://fonts.googleapis.com/css2?family=Lexend:wght@300&family=Playfair+Display:wght@700;900&family=Mr+Dafoe&display=swap">
<style>
  :root {
    --board-bg: #fdc0ae;
    --label-ink: #1c1c1c;
    --title-dark: #2a2a2a;
    --title-bronze: #8a5a23;
    --author-white: #ffffff;
    --author-cream: #f7dcc0;
    --art-top: #fcf8f3;
    --art-warm: #f4d7b8;
    --art-glow: #ffe2a8;
    --art-orange: #e8893a;
    --art-lilac: #a58bae;
    --art-plum: #4b3848;
    --art-night: #120e12;
    --cover-shadow: rgba(90, 45, 35, 0.55);
  }
  * { margin: 0; padding: 0; box-sizing: border-box; }
  html, body {
    width: 1200px;
    height: 1043px;
    overflow: hidden;
    background: var(--board-bg);
  }
  .board {
    position: relative;
    width: 1200px;
    height: 1043px;
  }
  .option-label {
    position: absolute;
    top: 62px;
    width: 513px;
    text-align: center;
    font-family: "Lexend", sans-serif;
    font-weight: 300;
    font-size: 50px;
    letter-spacing: 1px;
    color: var(--label-ink);
  }
  .cover {
    position: absolute;
    top: 156px;
    width: 513px;
    height: 769px;
    overflow: hidden;
    box-shadow: 22px 26px 18px var(--cover-shadow);
  }
  .option-one { left: 56px; }
  .option-two { left: 626px; }
  .cover-art {
    position: absolute;
    inset: 0;
    background:
      radial-gradient(ellipse 26% 18% at 68% 66%, var(--art-glow) 0%, rgba(255, 200, 120, 0.85) 35%, rgba(232, 137, 58, 0) 100%),
      radial-gradient(ellipse 62% 40% at 70% 66%, rgba(232, 137, 58, 0.85) 0%, rgba(165, 139, 174, 0.7) 55%, rgba(165, 139, 174, 0) 100%),
      radial-gradient(ellipse 40% 60% at 100% 55%, rgba(120, 100, 130, 0.55) 0%, rgba(120, 100, 130, 0) 100%),
      linear-gradient(180deg, var(--art-top) 0%, var(--art-top) 22%, var(--art-warm) 48%, var(--art-lilac) 68%, var(--art-plum) 84%, var(--art-night) 100%);
  }
  .cover-text {
    position: absolute;
    inset: 0;
    text-align: center;
  }
  .title {
    position: absolute;
    top: 186px;
    left: 0;
    right: 14px;
    font-family: "Playfair Display", serif;
    font-weight: 900;
    line-height: 1;
  }
  .title-lead {
    display: block;
    font-size: 42px;
    margin-bottom: 12px;
    padding-left: 16px;
  }
  .title-main {
    display: block;
    font-size: 72px;
    line-height: 66px;
    letter-spacing: -0.5px;
  }
  .subtitle {
    position: absolute;
    top: 364px;
    left: 0;
    right: 14px;
    font-family: "Mr Dafoe", cursive;
    font-size: 34px;
    color: var(--label-ink);
  }
  .author {
    position: absolute;
    top: 862px;
    top: 706px;
    left: 0;
    right: 0;
    font-family: "Playfair Display", serif;
    font-weight: 700;
    font-size: 37px;
    letter-spacing: -0.5px;
  }
  .option-one .title { color: var(--title-dark); }
  .option-one .author { color: var(--author-white); }
  .option-two .title { color: var(--title-bronze); }
  .option-two .author { color: var(--author-cream); }
</style>
</head>
<body>
  <main class="board">
    <h2 class="option-label" style="left:56px;">Model 01</h2>
    <h2 class="option-label" style="left:626px;">Model 02</h2>

    <section class="cover option-one">
      <div class="cover-art" role="img" aria-label="Illustration of bright multicoloured crystals bursting outward from a glowing golden centre toward the lower right, on a white-to-dark background"></div>
      <div class="cover-text">
        <h1 class="title">
          <span class="title-lead">THE</span>
          <span class="title-main">WOVEN</span>
          <span class="title-main">LANTERN</span>
        </h1>
        <p class="subtitle">Along Quiet Rivers</p>
        <p class="author">AUTHOR NAME</p>
      </div>
    </section>

    <section class="cover option-two">
      <div class="cover-art" role="img" aria-label="Illustration of bright multicoloured crystals bursting outward from a glowing golden centre toward the lower right, on a white-to-dark background"></div>
      <div class="cover-text">
        <h1 class="title">
          <span class="title-lead">THE</span>
          <span class="title-main">WOVEN</span>
          <span class="title-main">LANTERN</span>
        </h1>
        <p class="subtitle">Along Quiet Rivers</p>
        <p class="author">AUTHOR NAME</p>
      </div>
    </section>
  </main>
</body>
</html>
```